Etiketten für Brennerei aus Tirol
Zielgruppe
Wir sind eine Brennerei aus Tirol bzw. Südtirol, produzieren in Österreich hochwertige Obstbrände und beliefern mit unseren Bränden, Schnäpsen und Spirituosen den Lebensmittel Einzelhandel (kein Discount) in Österreich und Deutschland. Zielkunden sind Genießer, die die österreichische bzw. Südtiroler Gastlichkeit und Lebenskultur schätzen.
Für eine neue Produktlinie mit Gin / Whisky und Wodka möchten wir ein ganz neues Etikettendesign umsetzen.
Aufgabenstellung
Beiliegend Abbildung der Flasche und Skizze.
Wir möchten Tiroler Werte vemritteln -
Ehrlich kantig authentisch , naturverbunden, autonom
Tiroler Symbole können eingesetzt werden.
Stichworte: Manufaktur, Handcrafted
Bezeichnungen: Handcrafted Dry Gin, Premium Whiskey, Premium Wodka
Technik:
Rundumetikett oder
Ätzdruck auf Flasche

```html
<!DOCTYPE html>
<html lang="de">
<head>
<meta charset="utf-8">
<title>Etiketten – Whiskey, Dry Gin, Wodka</title>
<link href="https://fonts.googleapis.com/css2?family=Lilita+One&family=Oswald:wght@500&family=Fira+Sans:wght@800&family=Allura&display=swap" rel="stylesheet">
<style>
  :root{
    --page:#ffffff;
    --whiskey-band:#f4b57a;
    --whiskey-top:#f8d2ad;
    --whiskey-ink:#c0391b;
    --gin-band:#c99590;
    --gin-top:#e4eaea;
    --gin-ink:#eef1f1;
    --gin-mark:#a86a66;
    --wodka-band:#97a3cf;
    --wodka-top:#e6ebf0;
    --wodka-ink:#f3f5f8;
    --wodka-mark:#7d89c2;
  }
  *{margin:0;padding:0;box-sizing:border-box}
  html,body{width:1200px;height:562px;overflow:hidden;background:var(--page)}
  .canvas{position:relative;width:1200px;height:562px}
  .label{position:absolute;top:205px;width:154px;height:197px;overflow:hidden;background:var(--top)}
  .label--whiskey{left:77px;--top:var(--whiskey-top);--band:var(--whiskey-band);--ink:var(--whiskey-ink);--mark:var(--whiskey-ink)}
  .label--gin{left:508px;--top:var(--gin-top);--band:var(--gin-band);--ink:var(--gin-ink);--mark:var(--gin-mark)}
  .label--wodka{left:913px;--top:var(--wodka-top);--band:var(--wodka-band);--ink:var(--wodka-ink);--mark:var(--wodka-mark)}

  .brand{position:absolute;top:6px;left:0;width:100%;text-align:center;color:var(--mark)}
  .brand__dot{display:block;width:12px;height:12px;border-radius:50%;background:var(--mark);margin:0 auto 6px}
  .brand__name{font-family:'Oswald',sans-serif;font-weight:500;font-size:12px;letter-spacing:.5px;line-height:1}
  .brand__sub{font-family:'Oswald',sans-serif;font-weight:500;font-size:6.5px;letter-spacing:1px;line-height:1;margin-top:3px}

  .mountains{position:absolute;top:64px;left:0;width:100%;height:72px;
    background:linear-gradient(180deg,var(--top) 0%,var(--mark) 55%,var(--band) 100%);opacity:.85}
  .band{position:absolute;top:134px;left:0;width:100%;height:63px;background:var(--band)}
  .seal{position:absolute;top:96px;right:4px;width:42px;height:42px;border-radius:50%;background:var(--mark);opacity:.9}

  .kicker{position:absolute;left:0;width:100%;text-align:center;font-family:'Fira Sans',sans-serif;font-weight:800;font-size:7.5px;color:var(--ink)}
  .name{position:absolute;left:0;width:100%;text-align:center;font-family:'Lilita One',sans-serif;color:var(--ink);line-height:1}
  .label--whiskey .kicker{top:131px}
  .label--whiskey .name{top:142px;font-size:31px}
  .label--gin .kicker{top:121px;left:-30px}
  .label--gin .name{top:128px;font-size:44px}
  .label--wodka .kicker{top:131px}
  .label--wodka .name{top:142px;font-size:29px}

  .crafted{position:absolute;top:177px;left:10px;right:10px;display:flex;align-items:center;gap:6px;color:var(--ink)}
  .crafted::before,.crafted::after{content:"";flex:1;height:1px;background:var(--ink)}
  .crafted span{font-family:'Allura',cursive;font-size:10px;line-height:1}
</style>
</head>
<body>
<main class="canvas">
  <section class="label label--whiskey">
    <div class="brand"><span class="brand__dot"></span><div class="brand__name">ALPINERA</div><div class="brand__sub">BERGFEINKOST</div></div>
    <div class="mountains" role="img" aria-label="Gezeichnetes Bergpanorama der Alpen"></div>
    <div class="band"></div>
    <div class="seal" role="img" aria-label="Qualitätssiegel"></div>
    <div class="kicker">Premium</div>
    <div class="name">Whiskey</div>
    <div class="crafted"><span>handcrafted</span></div>
  </section>

  <section class="label label--gin">
    <div class="brand"><span class="brand__dot"></span><div class="brand__name">ALPINERA</div><div class="brand__sub">BERGFEINKOST</div></div>
    <div class="mountains" role="img" aria-label="Gezeichnetes Bergpanorama der Alpen"></div>
    <div class="band"></div>
    <div class="seal" role="img" aria-label="Qualitätssiegel"></div>
    <div class="kicker">Dry</div>
    <div class="name">Gin</div>
    <div class="crafted"><span>handcrafted</span></div>
  </section>

  <section class="label label--wodka">
    <div class="brand"><span class="brand__dot"></span><div class="brand__name">ALPINERA</div><div class="brand__sub">BERGFEINKOST</div></div>
    <div class="mountains" role="img" aria-label="Gezeichnetes Bergpanorama der Alpen"></div>
    <div class="band"></div>
    <div class="seal" role="img" aria-label="Qualitätssiegel"></div>
    <div class="kicker">Premium</div>
    <div class="name">Wodka</div>
    <div class="crafted"><span>handcrafted</span></div>
  </section>
</main>
</body>
</html>
```